Urgent - brand new business card for a startup technical advisory and incubation business in Sydney

We need a brand new business card design for BrightForge. We are a startup technical advisory and incubation business based in Sydney Australia. We work with entrepreneurs and innovators to help rapidly and efficiently turn their ideas into reality and to ensure they have the technical platform required for growth.

Our name is partly inspired by our love of lean product development methods and the lean startup movement.

We would like clean, uncluttered designs that feature our two logo colours and communicate a professional but creative, in-touch and entrepreneurial business.

PLEASE SEE MUST HAVE PRIORITIES FOR DRAFT CONTACT INFORMATION AND OTHER DESIRED TEXT ON CARD.
Updates

We have now updated the brief to include draft business card contact information and also some additional desired text to feature on the card design.    Please review the Must Have priorities.

Also final updated source files for the horizontal and vertical versions have now been uploaded and should be used for any designs.

Thanks!

Target Market(s)

Entrepeneurs, innovators, startup investors looking for a strong product development partner

Industry/Entity Type

Business

Requirements
Must have
• Feature our two logo colours
Be a relatively clean, pared back overall design - quite minimalist

Updated source files (AI) for vertical and horizontal layouts attached.

Draft contact information for business card:
Neil Barton
Founder & CTO
Phone: +61 427 555123
Email: xxxx@brightforge.com
Skype: xxxxxbarton
Twitter: nbarton

www.brightforge.com

We would also like the overall design to include the phrase "You have great ideas. Let us make them happen." (probably in a reasonably subtle way)

Nice to have
• Inspire me! Double-sided designs are fine with logo, phrase, (URL?) on one side and contact details on other (+ any other design elements)

Logo on business card can be either with lightbulb above the wording as per example here or to the left of the BrightForge wording - both layouts in files provided.
Should not have
• Shouldn't look like a Pentara Suite business card template :-)

```html
<!DOCTYPE html>
<html lang="en">
<head>
<meta charset="utf-8">
<title>BrightForge Business Card</title>
<link rel="stylesheet" href="https://fonts.googleapis.com/css2?family=Open+Sans:wght@300;400;700&display=swap">
<style>
  :root {
    --stage: #e9e7e3;
    --card: #ffffff;
    --card-edge: #dcdcdc;
    --brand-blue: #2ba3d1;
    --wave-light: #35b6dc;
    --wave-mid: #1f7fb8;
    --wave-deep: #1a5f93;
    --wave-navy: #0f2140;
    --wave-slate: #2b3f66;
    --ink: #3a3d42;
    --ink-soft: #6b6e73;
  }
  * { margin: 0; padding: 0; box-sizing: border-box; }
  html, body {
    width: 1200px; height: 1023px; overflow: hidden;
    background: var(--stage);
    font-family: "Open Sans", Arial, sans-serif;
  }
  .sheet {
    width: 1200px; height: 1023px;
    display: flex; flex-direction: column; align-items: center; justify-content: center;
    gap: 22px;
  }
  .card {
    position: relative;
    width: 840px; height: 480px;
    background: var(--card);
    border: 1px solid var(--card-edge);
    box-shadow: 0 6px 18px rgba(0,0,0,0.12);
    overflow: hidden;
  }
  /* contact side */
  .card-waves { position: absolute; left: 0; top: 0; width: 840px; height: 480px; }
  .brand {
    position: absolute; right: 48px; top: 40px;
    display: flex; align-items: center; gap: 12px;
  }
  .brand-dot { width: 34px; height: 34px; border-radius: 50%; background: var(--brand-blue); }
  .brand-name { font-weight: 700; font-size: 34px; color: var(--brand-blue); letter-spacing: -0.5px; }
  .person { position: absolute; right: 48px; top: 128px; text-align: right; }
  .person-name { font-weight: 400; font-size: 24px; color: var(--brand-blue); letter-spacing: 0.5px; }
  .person-title { font-weight: 300; font-size: 17px; color: var(--ink-soft); margin-top: 2px; }
  .contact-list { position: absolute; right: 48px; top: 230px; list-style: none; text-align: right; }
  .contact-item {
    display: flex; justify-content: flex-end; align-items: center; gap: 12px;
    font-weight: 300; font-size: 17px; color: var(--ink-soft); line-height: 34px;
  }
  .contact-icon { width: 18px; height: 18px; flex: none; }
  /* logo side */
  .card-back { display: flex; align-items: center; justify-content: center; gap: 26px;
    background: linear-gradient(180deg, #ffffff 0%, #f1f1f1 100%); }
  .back-dot { width: 96px; height: 96px; border-radius: 50%; background: var(--brand-blue); }
  .back-name { font-weight: 700; font-size: 96px; color: var(--ink); letter-spacing: -2px; }
</style>
</head>
<body>
<main class="sheet">
  <section class="card card-front">
    <svg class="card-waves" viewBox="0 0 840 480" aria-hidden="true">
      <path d="M0 0 H300 C180 120 150 300 230 480 H0 Z" fill="var(--wave-light)"/>
      <path d="M0 0 H250 C150 120 120 300 185 480 H0 Z" fill="var(--wave-mid)"/>
      <path d="M0 0 H210 C120 130 95 300 150 480 H0 Z" fill="var(--wave-deep)"/>
      <path d="M0 0 H175 C95 130 75 300 120 480 H0 Z" fill="var(--wave-navy)"/>
      <path d="M0 0 H145 C75 130 55 300 95 480 H0 Z" fill="var(--wave-slate)"/>
      <path d="M0 0 H110 C50 130 35 300 70 480 H0 Z" fill="var(--wave-mid)"/>
      <path d="M0 0 H80 C30 130 20 300 45 480 H0 Z" fill="var(--wave-light)"/>
    </svg>
    <div class="brand">
      <span class="brand-dot"></span>
      <span class="brand-name">BrightForge</span>
    </div>
    <div class="person">
      <p class="person-name">JOHN DOE SMITH</p>
      <p class="person-title">Title</p>
    </div>
    <ul class="contact-list">
      <li class="contact-item">Adress
        <svg class="contact-icon" viewBox="0 0 18 18"><path d="M6 3 L12 9 L6 15" fill="none" stroke="var(--wave-deep)" stroke-width="3"/></svg>
      </li>
      <li class="contact-item">Phone
        <svg class="contact-icon" viewBox="0 0 18 18"><rect x="1" y="1" width="16" height="16" rx="3" fill="var(--wave-deep)"/><path d="M5 4 L7 4 L8 7 L6.5 8 C7.5 10 8.5 11 10 11.5 L11 10 L14 11 L14 13 C9 14 4 9 5 4 Z" fill="#fff"/></svg>
      </li>
      <li class="contact-item">yourcompany@site.com
        <svg class="contact-icon" viewBox="0 0 18 18"><circle cx="9" cy="9" r="8" fill="var(--wave-deep)"/><path d="M9 4 V14 M4 9 H14" stroke="#fff" stroke-width="1.5"/></svg>
      </li>
      <li class="contact-item">www.companyname.com
        <svg class="contact-icon" viewBox="0 0 18 18"><rect x="1" y="3" width="16" height="12" fill="var(--wave-deep)"/><path d="M2 4 L9 10 L16 4" fill="none" stroke="#fff" stroke-width="1.5"/></svg>
      </li>
    </ul>
  </section>

  <section class="card card-back">
    <span class="back-dot"></span>
    <span class="back-name">BrightForge</span>
  </section>
</main>
</body>
</html>
```